Stationary Set Rebrand for Brenvik

We are a Canadian Distribution and Service Company that was established in 1969. Over the past 5 decades we have expanded our business and have warehouses across Canada. We specialize in adhesive tapes, adhesives, films, safety, warehouse, shipping, janitorial and packaging supplies.

We have updated our logo design and would like a new corporate branding identity that includes a new fresh Stationary Set (Business Cards, Letterhead, Letterhead MS Word, Envelope, Presentation Folders, Email Signatures, Notepad Covers, etc.)

Target Market(s)

Industrial Business Sector

Font styles to use
Sans Serif

Colors
0054AA
0677BA
7BADD7
CADEEF
E8F1F8
0094D4
00A9DD
6FCCEA
C7EBF8
E9F6FB
00AB8E
00BBA5
67D7C9
C6EFE9
E9F9F6
EB3D1F
EC4F4E
F09395
F8D3D4
FCEDEE

Requirements
Should not have
• Colors not too light, darker colours preferred

```html
<!DOCTYPE html>
<html lang="en">
<head>
<meta charset="utf-8">
<title>Brenvik Business Card</title>
<link rel="stylesheet" href="https://fonts.googleapis.com/css2?family=Open+Sans:wght@400;600;800&display=swap">
<style>
  :root {
    --stage: #1b1b1d;
    --brand-red: #d71920;
    --brand-red-dark: #b3121a;
    --brand-red-light: #f2474c;
    --ink: #1c1c1c;
    --muted: #555559;
    --rule: #6d6d70;
    --paper: #ffffff;
  }
  * { box-sizing: border-box; margin: 0; padding: 0; }
  html, body {
    width: 1200px; height: 900px; overflow: hidden;
    background: var(--stage);
    font-family: "Open Sans", Arial, sans-serif;
  }
  .stage {
    width: 1200px; height: 900px;
    display: flex; flex-direction: column;
    align-items: center; justify-content: center; gap: 34px;
  }
  .card {
    position: relative;
    width: 680px; height: 389px;
    overflow: hidden;
    box-shadow: 0 10px 30px rgba(0,0,0,.55);
  }

  /* Front */
  .card--front { background: var(--paper); }
  .holder { position: absolute; left: 52px; top: 56px; }
  .holder__name {
    color: var(--brand-red); font-weight: 600;
    font-size: 25px; letter-spacing: .5px; text-transform: uppercase; line-height: 1.1;
  }
  .holder__title { color: var(--muted); font-size: 19px; margin-top: 4px; }
  .divider {
    position: absolute; left: 50px; right: 40px; top: 140px;
    height: 1.5px; background: var(--rule);
  }
  .wordmark {
    position: absolute; right: 56px; top: 52px;
    font-weight: 800; font-size: 68px; line-height: 1;
    color: var(--ink); letter-spacing: -1px;
  }
  .contact { position: absolute; left: 52px; top: 162px; list-style: none; }
  .contact__item {
    display: flex; align-items: center; gap: 10px;
    color: var(--muted); font-size: 18px; line-height: 1.55;
  }
  .contact__icon { width: 16px; height: 16px; flex: none; }
  .address {
    position: absolute; right: 56px; top: 262px;
    text-align: right; color: var(--muted); font-size: 18px; line-height: 1.4;
  }
  .edge-band { position: absolute; left: 0; bottom: 0; width: 100%; height: 24px; }

  /* Back */
  .card--back { background: var(--brand-red); }
  .emblem-area {
    position: absolute; left: -40px; top: -60px;
    width: 360px; height: 380px; border-radius: 50%;
    background: radial-gradient(circle at 60% 55%, var(--brand-red-light) 0%, var(--brand-red-dark) 55%, rgba(179,18,26,0) 72%);
  }
  .card--back .wordmark { color: var(--paper); top: 58px; right: 48px; }
</style>
</head>
<body>
<main class="stage">

  <section class="card card--front" aria-label="Business card front">
    <div class="holder">
      <p class="holder__name">Marcus Hale</p>
      <p class="holder__title">Managing Director</p>
    </div>
    <p class="wordmark">Brenvik</p>
    <div class="divider"></div>

    <ul class="contact">
      <li class="contact__item">
        <svg class="contact__icon" viewBox="0 0 16 16"><circle cx="8" cy="8" r="8" fill="#d71920"/><path d="M5 4.5c.5-.4 1-.3 1.3.2l.6 1.1c.2.4 0 .8-.3 1l-.4.3c.4.9 1.1 1.6 2 2l.3-.4c.2-.3.6-.5 1-.3l1.1.6c.5.3.6.8.2 1.3-.6.7-1.5.9-2.4.5C6.6 10 5.9 9.3 5.1 7.4c-.4-.9-.3-2.2-.1-2.9z" fill="#fff"/></svg>
        044-123 456 789
      </li>
      <li class="contact__item">
        <svg class="contact__icon" viewBox="0 0 16 16"><circle cx="8" cy="8" r="8" fill="#d71920"/><rect x="4" y="5" width="8" height="6" rx=".6" fill="#fff"/><path d="M4.3 5.4 8 8.3l3.7-2.9" fill="none" stroke="#d71920" stroke-width="1"/></svg>
        info@brenvik-supply.com
      </li>
      <li class="contact__item">
        <svg class="contact__icon" viewBox="0 0 16 16"><circle cx="8" cy="8" r="8" fill="#d71920"/><circle cx="8" cy="8" r="4" fill="none" stroke="#fff" stroke-width="1.1"/><path d="M4 8h8M8 4c-1.6 2.2-1.6 5.8 0 8M8 4c1.6 2.2 1.6 5.8 0 8" fill="none" stroke="#fff" stroke-width=".9"/></svg>
        www.brenvik-supply.com
      </li>
    </ul>

    <p class="address">Your Address, City<br>State, Zip 0000</p>

    <svg class="edge-band" viewBox="0 0 680 24" preserveAspectRatio="none" aria-hidden="true">
      <polygon points="0,10 250,10 244,24 0,24" fill="#1c1c1c"/>
      <polygon points="256,0 680,0 680,24 244,24" fill="#d71920"/>
    </svg>
  </section>

  <section class="card card--back" aria-label="Business card back">
    <div class="emblem-area" role="img" aria-label="Large embossed brand emblem in deep red tones"></div>
    <p class="wordmark">Brenvik</p>
  </section>

</main>
</body>
</html>
```